Online Marketing Agency Website

We are an online marketing agency that specializes in search marketing (SEM) for businesses of all sizes. Our core services include local search marketing, seo, paid search, paid social, graphic design, video production/editing and website design. We have an existing website that we launched a number of years ago but it's very outdated and we're currently too busy to design a new version.

Target Market(s)

Any business that needs online marketing services with an emphasis on search marketing.

Industry/Entity Type

Ad Agency

Number of Pages Required

4 page

Font styles to use
Sans Serif

Requirements
Must have
• Home page, interior page, blog page, contact us page.
Look and feel should be modern and clean and easy to navigate.
Sections for call outs for specific services: Business Marketing Strategy, Content Creation and Marketing, Graphic & Publication Design, Pay Per Click (PPC) Management, Search Engine Optimization, Social Media Management, Video Production & Editing, Website Hosting & Management, Website Design & Development
Use color from logo that was uploaded.

```html
<!DOCTYPE html>
<html lang="en">
<head>
<meta charset="utf-8">
<title>Ascent Digital — Online Marketing</title>
<link href="https://fonts.googleapis.com/css2?family=Montserrat:wght@400;500;600;700&family=Lato:wght@400;700&display=swap" rel="stylesheet">
<style>
:root{
  --orange:#ff6633;
  --orange-light:#ff7a4d;
  --ink:#222;
  --text:#333;
  --muted:#666;
  --card:#f7f7f7;
  --line:#e6e6e6;
  --white:#fff;
}
*{box-sizing:border-box;margin:0;padding:0}
html,body{width:1200px;height:3529px;overflow:hidden}
body{position:relative;font-family:'Lato',sans-serif;color:var(--text);background:var(--white)}
.abs{position:absolute}
.heading{font-family:'Montserrat',sans-serif}

/* top bar */
.topbar{left:0;top:0;width:1200px;height:30px;background:var(--orange)}
.social{left:158px;top:8px;display:flex;gap:8px}
.social span{width:14px;height:14px;border-radius:50%;background:var(--white);display:block}
.callus{right:146px;top:7px;color:var(--white);font-size:12px;display:flex;align-items:center;gap:6px;font-family:'Montserrat',sans-serif}

/* nav */
.brand{left:156px;top:45px;font-family:'Montserrat',sans-serif;font-weight:600;color:var(--orange);font-size:15px;display:flex;align-items:center;gap:6px}
.brand i{width:14px;height:14px;border-radius:50%;background:var(--orange);display:block}
.nav{right:150px;top:47px;display:flex;gap:40px;font-family:'Montserrat',sans-serif;font-size:12px;color:var(--ink)}

/* hero */
.hero-photo{left:590px;top:75px;width:610px;height:455px;background:linear-gradient(90deg,#fff 0%,#e9e6e3 18%,#b9aea5 55%,#6e625a 100%)}
.hero-title{left:148px;top:193px;font-size:42px;font-weight:600;color:var(--orange)}
.hero-copy{left:150px;top:256px;width:510px;font-size:15px;line-height:22px;color:var(--orange)}
.btn-small{left:150px;top:367px;width:158px;height:37px;background:var(--orange);color:var(--white);font-size:13px;display:flex;align-items:center;justify-content:center;border-radius:2px}
.band{left:0;top:530px;width:1200px;height:52px;background:var(--orange);color:var(--white);text-align:center}
.band h3{font-family:'Montserrat',sans-serif;font-weight:500;font-size:14px;margin-top:8px}
.band p{font-size:9.5px;margin-top:4px}

/* what we do */
.desk-photo{left:89px;top:666px;width:489px;height:326px;background:linear-gradient(135deg,#8a857f,#d9d6d2 45%,#bcb7b1)}
.what-title{left:668px;top:715px;font-size:48px;font-weight:600;color:var(--orange)}
.what-copy{left:669px;top:792px;width:400px;font-size:15.5px;line-height:26.5px;color:var(--ink)}

/* services */
.section-title{width:1200px;left:0;text-align:center;color:var(--orange);font-weight:600}
.services-title{top:1096px;font-size:38px}
.underline{left:506px;top:1157px;width:188px;height:3px;background:var(--orange)}
.card{width:202px;height:234px;background:var(--card);border:2px solid var(--line);border-radius:6px;padding:20px 18px}
.card svg{display:block;height:46px;width:46px}
.card h4{font-family:'Montserrat',sans-serif;font-weight:500;font-size:14.5px;line-height:19px;color:var(--ink);margin-top:14px;height:38px}
.card p{font-size:12px;line-height:18px;color:var(--ink);margin-top:13px}
.card .more{font-size:13px;color:var(--ink);position:absolute;left:18px;bottom:14px;font-family:'Montserrat',sans-serif}
.card.active{background:var(--orange);border-color:var(--orange)}
.card.active h4,.card.active p,.card.active .more{color:var(--white)}
.btn-explore{left:456px;top:1777px;width:288px;height:55px;background:var(--orange);border-radius:12px;color:var(--white);font-family:'Montserrat',sans-serif;font-weight:500;font-size:15px;display:flex;align-items:center;justify-content:center;letter-spacing:.5px}

/* featured */
.featured{left:0;top:1952px;width:1200px;height:459px;background:var(--orange)}
.featured-title{top:1970px;color:var(--white);font-size:26px}
.work{top:2025px;width:243px;height:334px;background:var(--white);border-radius:4px;padding:12px 10px;text-align:center}
.work .thumb{height:192px;border-radius:6px}
.work h5{font-family:'Montserrat',sans-serif;font-weight:600;font-size:14px;color:var(--ink);margin-top:20px;line-height:15px}
.work p{font-size:13px;line-height:15px;color:var(--ink);margin-top:12px}
.arrow-btn{top:2156px;width:66px;height:66px;border-radius:50%;background:var(--white)}

/* clients */
.clients-title{top:2525px;width:1200px;left:0;text-align:center;font-size:22px;font-weight:400;color:var(--ink);font-family:'Montserrat',sans-serif}
.clients-title b{font-weight:700}
.chev{top:2564px}
.review{top:2610px;width:272px;height:168px;background:var(--white);border:2px solid #eee;box-shadow:0 2px 8px rgba(0,0,0,.06);padding:20px 18px}
.avatar{width:52px;height:52px;border-radius:50%;background:#c9b8a8}
.review .who{position:absolute;left:82px;top:22px;font-family:'Montserrat',sans-serif;font-size:14px;color:var(--ink);line-height:17px}
.review .who span{font-size:12.5px;display:block}
.review p{font-size:11.5px;line-height:15px;color:var(--muted);margin-top:18px}
.stars{color:#f5b400;font-size:15px;letter-spacing:2px;margin-top:4px}

/* contact */
.contact-photo{left:670px;top:2850px;width:530px;height:397px;background:linear-gradient(90deg,#fff 0%,#e7d7c8 30%,#b49580 70%,#8c6f5e 100%)}
.lift{left:0;width:830px;top:2878px;text-align:center;font-size:40px;font-weight:600;color:var(--orange)}
.contact-h{left:0;width:830px;top:2925px;text-align:center;font-size:50px;font-weight:600;color:#3a3a3a}
.contact-sub{left:0;width:830px;top:2990px;text-align:center;font-size:14px;color:var(--ink)}
.field{left:159px;width:241px;height:41px;border:1px solid #ccc;background:var(--white);padding:12px 14px;font-size:13px;color:#999}
.message{left:414px;top:3022px;width:263px;height:140px;border:1px solid #ccc;background:var(--white);padding:10px 10px;font-size:13px;color:#999}
.send{left:159px;top:3173px;width:518px;height:40px;background:var(--orange);color:var(--white);font-size:18px;font-family:'Montserrat',sans-serif;display:flex;align-items:center;justify-content:center}

/* footer */
.footer{left:0;top:3271px;width:1200px;height:258px;background:var(--orange)}
.footer-brand{left:150px;top:3368px;display:flex;align-items:center;gap:10px;font-family:'Montserrat',sans-serif;font-weight:600;font-size:20px;color:var(--white)}
.footer-brand i{width:16px;height:16px;border-radius:50%;background:var(--white);display:block}
.col-title{top:3325px;color:var(--white);font-family:'Montserrat',sans-serif;font-size:17px;font-weight:500}
.links{top:3370px;display:grid;grid-template-columns:128px 100px;row-gap:9px;color:var(--white);font-size:12px}
.links span{display:flex;align-items:center;gap:7px}
.links svg{width:17px;height:17px}
.copyright{left:0;top:3492px;width:1200px;text-align:center;color:var(--white);font-size:12.5px;font-family:'Montserrat',sans-serif}
</style>
</head>
<body>

<div class="abs topbar"></div>
<div class="abs social" aria-label="Social links"><span></span><span></span><span></span></div>
<div class="abs callus">
  <svg width="13" height="14" viewBox="0 0 24 24" fill="#fff"><path d="M6.6 10.8a15 15 0 0 0 6.6 6.6l2.2-2.2c.3-.3.7-.4 1-.2 1.1.4 2.3.6 3.6.6.6 0 1 .4 1 1V20c0 .6-.4 1-1 1A17 17 0 0 1 3 4c0-.6.4-1 1-1h3.5c.6 0 1 .4 1 1 0 1.3.2 2.5.6 3.6.1.3 0 .7-.2 1z"/></svg>
  Call us at 800-555-0142
</div>

<div class="abs brand"><i></i>Ascent Digital</div>
<nav class="abs nav"><span>Home</span><span>Our Services</span><span>Featured Work</span><span>Blog</span><span>About</span><span>Contact</span></nav>

<div class="abs hero-photo" role="img" aria-label="Photo of a smiling team gathered around a laptop"></div>
<h1 class="abs heading hero-title">Marketing done right</h1>
<p class="abs hero-copy">Lorem ipsum dolor sit amet, consectetur adipiscing elit, sed do eiusmod tempor incididunt ut labore et dolore magna aliqua. Ut enim ad minim veniam, quis nostrud exercitation ullamco laboris nisi ut</p>
<div class="abs btn-small">Contact Us</div>

<div class="abs band">
  <h3>LOCAL SEO AND BUSINESS LISTINGS</h3>
  <p>85% of Consumers use the Internet to find local businesses. Are they finding yours?</p>
</div>

<div class="abs desk-photo" role="img" aria-label="Photo of a desk with a laptop, glasses and a notebook"></div>
<h2 class="abs heading what-title">What we do ?</h2>
<p class="abs what-copy">Ascent Digital is a full-service online marketing agency. We can handle any element of your online marketing so you can get back to doing what you do best&nbsp; growing your business. All of our services are offered on an ‘a la carte’ basis.</p>

<h2 class="abs heading section-title services-title">Our Services</h2>
<div class="abs underline"></div>

<!-- service cards row 1 -->
<div class="abs card" style="left:147px;top:1222px">
  <svg viewBox="0 0 48 48" fill="none" stroke="var(--orange)" stroke-width="2"><rect x="4" y="30" width="7" height="14"/><rect x="16" y="24" width="7" height="20"/><rect x="28" y="18" width="7" height="26"/><rect x="40" y="12" width="6" height="32"/><path d="M4 20 20 6M14 6h6v6"/></svg>
  <h4>Business Marketing<br>Strategy</h4>
  <p>Lorem ipsum dolor sit amet, consectetur adipiscing elit, sed do eiusmod tempor</p>
  <span class="more">Read More</span>
</div>
<div class="abs card" style="left:381px;top:1222px">
  <svg viewBox="0 0 48 48" fill="none" stroke="var(--orange)" stroke-width="2"><rect x="3" y="4" width="36" height="34"/><path d="M3 11h36M8 17h14M8 23h14M8 29h10"/><rect x="26" y="16" width="9" height="9"/><circle cx="38" cy="38" r="6"/></svg>
  <h4>Content Creation<br>And Marketing</h4>
  <p>Lorem ipsum dolor sit amet, consectetur adipiscing elit, sed do eiusmod tempor</p>
  <span class="more">Read More</span>
</div>
<div class="abs card active" style="left:616px;top:1222px">
  <svg viewBox="0 0 48 48" fill="none" stroke="#fff" stroke-width="2"><rect x="3" y="12" width="42" height="26"/><path d="M10 30V20M17 30V14M24 30V18M31 30V10M38 30V22M18 38l-3 6h18l-3-6"/></svg>
  <h4>Graphic And<br>Publication Design</h4>
  <p>Lorem ipsum dolor sit amet, consectetur adipiscing elit, sed do eiusmod tempor</p>
  <span class="more">Read More</span>
</div>
<div class="abs card" style="left:849px;top:1222px">
  <svg viewBox="0 0 48 48" fill="none" stroke="var(--orange)" stroke-width="2"><circle cx="26" cy="13" r="10"/><path d="M26 7v12M23 10h5M23 16h5M10 22v14c0 5 4 9 9 9h4M10 22c0-3 5-3 5 0v8"/></svg>
  <h4>Pay Per Click (PPC)<br>Management</h4>
  <p>Lorem ipsum dolor sit amet, consectetur adipiscing elit, sed do eiusmod tempor</p>
  <span class="more">Read More</span>
</div>

<!-- service cards row 2 -->
<div class="abs card" style="left:147px;top:1485px">
  <svg viewBox="0 0 48 48" fill="none" stroke="var(--orange)" stroke-width="2"><rect x="3" y="6" width="34" height="26"/><circle cx="20" cy="19" r="7"/><path d="M18 16l5 3-5 3zM3 38h22M32 36h14M32 42h14"/></svg>
  <h4>Video Production<br>And Editing</h4>
  <p>Lorem ipsum dolor sit amet, consectetur adipiscing elit, sed do eiusmod tempor</p>
  <span class="more">Read More</span>
</div>
<div class="abs card" style="left:381px;top:1485px">
  <svg viewBox="0 0 48 48" fill="none" stroke="var(--orange)" stroke-width="2"><rect x="4" y="4" width="12" height="10"/><rect x="32" y="4" width="12" height="10"/><rect x="18" y="34" width="12" height="10"/><path d="M10 14v10h28V14M24 24v10"/></svg>
  <h4>Website Hosting<br>And Management</h4>
  <p>Lorem ipsum dolor sit amet, consectetur adipiscing elit, sed do eiusmod tempor</p>
  <span class="more">Read More</span>
</div>
<div class="abs card" style="left:616px;top:1485px">
  <svg viewBox="0 0 48 48" fill="none" stroke="var(--orange)" stroke-width="2"><rect x="3" y="14" width="42" height="24"/><path d="M3 20h42M14 38l-2 6h24l-2-6M20 6v8M28 10v4M36 4v10"/></svg>
  <h4>Website Design<br>And Development</h4>
  <p>Lorem ipsum dolor sit amet, consectetur adipiscing elit, sed do eiusmod tempor</p>
  <span class="more">Read More</span>
</div>
<div class="abs card" style="left:849px;top:1485px">
  <svg viewBox="0 0 48 48" fill="none" stroke="var(--orange)" stroke-width="2"><rect x="3" y="4" width="14" height="12"/><rect x="22" y="4" width="14" height="12"/><path d="M10 16v10M29 16v10M6 26h30v8H6zM14 34v10h12"/></svg>
  <h4>Social Media<br>Management</h4>
  <p>Lorem ipsum dolor sit amet, consectetur adipiscing elit, sed do eiusmod tempor</p>
  <span class="more">Read More</span>
</div>

<div class="abs btn-explore">Explore All Services</div>

<!-- featured work -->
<div class="abs featured"></div>
<h2 class="abs heading section-title featured-title">Featured Work</h2>
<div class="abs arrow-btn" style="left:118px">
  <svg width="66" height="66" viewBox="0 0 66 66" fill="none" stroke="var(--orange)" stroke-width="3"><path d="M38 18 24 33l14 15"/></svg>
</div>
<div class="abs arrow-btn" style="left:1015px">
  <svg width="66" height="66" viewBox="0 0 66 66" fill="none" stroke="var(--orange)" stroke-width="3"><path d="M28 18l14 15-14 15"/></svg>
</div>
<div class="abs work" style="left:212px">
  <div class="thumb" role="img" aria-label="Menu board artwork for a seafood restaurant promotion" style="background:linear-gradient(160deg,#5b2a8c,#c9501f 60%,#e8a23a)"></div>
  <h5>Digital Signage Content</h5>
  <p>Digital menu board content&nbsp; for Harbor Fish Shack Restaurants.</p>
</div>
<div class="abs work" style="left:482px">
  <div class="thumb" role="img" aria-label="Editorial spread artwork with a video camera theme" style="background:linear-gradient(135deg,#e9e9e9,#3aa0b0 55%,#e14a7a)"></div>
  <h5>Editorial Design</h5>
  <p>Editorial design for an internet marketing magazine.</p>
</div>
<div class="abs work" style="left:752px">
  <div class="thumb" role="img" aria-label="Mockup of business cards and letterhead on a dark desk" style="background:linear-gradient(135deg,#3a3d40,#8e9396 55%,#e6e8ea)"></div>
  <h5>Corpotate Identity<br>Development</h5>
  <p>Corporate Identity Development for Dana Reed Law.</p>
</div>

<!-- clients -->
<h2 class="abs clients-title">What Our <b>Clients Say</b></h2>
<svg class="abs chev" style="left:128px" width="20" height="30" viewBox="0 0 20 30" fill="none" stroke="#333" stroke-width="2.5"><path d="M15 3 4 15l11 12"/></svg>
<svg class="abs chev" style="left:1046px" width="20" height="30" viewBox="0 0 20 30" fill="none" stroke="#333" stroke-width="2.5"><path d="M5 3l11 12L5 27"/></svg>
<div class="abs review" style="left:-168px"></div>
<div class="abs review" style="left:147px">
  <div class="avatar" role="img" aria-label="Client portrait"></div>
  <div class="who">Jonathan Doe<span>lorem CEO</span></div>
  <p>Lorem ipsum dolor sit amet, consectetur adipiscing elit, sed do eiusmod tempor incididunt ut labore et dolore magna</p>
  <div class="stars">★★★★★</div>
</div>
<div class="abs review" style="left:462px">
  <div class="avatar" role="img" aria-label="Client portrait" style="background:#5c6b7d"></div>
  <div class="who">Jonathan Doe<span>lorem CEO</span></div>
  <p>Lorem ipsum dolor sit amet, consectetur adipiscing elit, sed do eiusmod tempor incididunt ut labore et dolore magna</p>
  <div class="stars">★★★★★</div>
</div>
<div class="abs review" style="left:777px">
  <div class="avatar" role="img" aria-label="Client portrait" style="background:#7d8f6a"></div>
  <div class="who">Jonathan Doe<span>lorem CEO</span></div>
  <p>Lorem ipsum dolor sit amet, consectetur adipiscing elit, sed do eiusmod tempor incididunt ut labore et dolore magna</p>
  <div class="stars">★★★★★</div>
</div>
<div class="abs review" style="left:1093px"></div>

<!-- contact -->
<div class="abs contact-photo" role="img" aria-label="Photo of hands typing on a laptop"></div>
<h2 class="abs heading lift">Need a lift ?</h2>
<h2 class="abs heading contact-h">Contact Us</h2>
<p class="abs contact-sub">Interested in working with us?&nbsp; Fill out the form below or give us a call!</p>
<div class="abs field" style="top:3022px">Full Name</div>
<div class="abs field" style="top:3072px">Phone Number</div>
<div class="abs field" style="top:3122px">Email Address</div>
<div class="abs message">Message</div>
<div class="abs send">Send Message</div>

<!-- footer -->
<div class="abs footer"></div>
<svg class="abs" style="left:0;top:3440px" width="1200" height="89" viewBox="0 0 1200 89"><path d="M0 89C300 30 800 10 1200 40V89Z" fill="var(--orange-light)"/></svg>
<div class="abs footer-brand"><i></i>Ascent Digital</div>

<div class="abs col-title" style="left:524px">COMPANY</div>
<div class="abs links" style="left:470px">
  <span><svg viewBox="0 0 24 24" fill="none" stroke="#fff" stroke-width="1.6"><path d="M3 11 12 3l9 8v10h-6v-6H9v6H3z"/></svg>Home</span>
  <span><svg viewBox="0 0 24 24" fill="none" stroke="#fff" stroke-width="1.6"><rect x="3" y="3" width="18" height="18"/><path d="M7 8h10M7 12h10M7 16h7"/></svg>Blog</span>
  <span><svg viewBox="0 0 24 24" fill="none" stroke="#fff" stroke-width="1.6"><path d="M4 14a8 8 0 0 1 16 0v4h-4v-5h4M4 13h4v5H4z"/></svg>Our Services</span>
  <span><svg viewBox="0 0 24 24" fill="none" stroke="#fff" stroke-width="1.6"><circle cx="12" cy="8" r="4"/><path d="M4 21c0-4 4-7 8-7s8 3 8 7"/></svg>About</span>
  <span><svg viewBox="0 0 24 24" fill="none" stroke="#fff" stroke-width="1.6"><rect x="3" y="7" width="18" height="13"/><path d="M8 7V4h8v3M3 12h18"/></svg>Featured Work</span>
  <span><svg viewBox="0 0 24 24" fill="none" stroke="#fff" stroke-width="1.6"><path d="M6 3h4l2 5-3 2a11 11 0 0 0 5 5l2-3 5 2v4a2 2 0 0 1-2 2A17 17 0 0 1 4 5a2 2 0 0 1 2-2z"/></svg>Contact</span>
</div>

<div class="abs col-title" style="left:900px">PROJECTS</div>
<div class="abs links" style="left:847px">
  <span><svg viewBox="0 0 24 24" fill="none" stroke="#fff" stroke-width="1.6"><path d="M3 11 12 3l9 8v10h-6v-6H9v6H3z"/></svg>Home</span>
  <span><svg viewBox="0 0 24 24" fill="none" stroke="#fff" stroke-width="1.6"><rect x="3" y="3" width="18" height="18"/><path d="M7 8h10M7 12h10M7 16h7"/></svg>Blog</span>
  <span><svg viewBox="0 0 24 24" fill="none" stroke="#fff" stroke-width="1.6"><path d="M4 14a8 8 0 0 1 16 0v4h-4v-5h4M4 13h4v5H4z"/></svg>Our Services</span>
  <span><svg viewBox="0 0 24 24" fill="none" stroke="#fff" stroke-width="1.6"><circle cx="12" cy="8" r="4"/><path d="M4 21c0-4 4-7 8-7s8 3 8 7"/></svg>About</span>
  <span><svg viewBox="0 0 24 24" fill="none" stroke="#fff" stroke-width="1.6"><rect x="3" y="7" width="18" height="13"/><path d="M8 7V4h8v3M3 12h18"/></svg>Featured Work</span>
  <span><svg viewBox="0 0 24 24" fill="none" stroke="#fff" stroke-width="1.6"><path d="M6 3h4l2 5-3 2a11 11 0 0 0 5 5l2-3 5 2v4a2 2 0 0 1-2 2A17 17 0 0 1 4 5a2 2 0 0 1 2-2z"/></svg>Contact</span>
</div>

<p class="abs copyright">COPYRIGHT © 2020 ASCENT DIGITAL LLC. ALL RIGHTS RESERVED.</p>

</body>
</html>
```